Stationery Design Project for Marketing Consultancy

I have started a new consultancy business and require the following elements to be designed using existing logo:
• Business card
• Letterhead
• Envelope (DL, C4, C5)
• Microsoft word template for report writing
• A4 Presentation Folder
• Powerpoint template
COPY FOR FRONT AND BACK OF BUSINESS CARD
logo
'Measurable Marketing. Epic Results' slogan (but no need to use existing lockup with logo)
name, B Comm, Grad Cert Brand Strategy, CMP (post nominal abbreviations in smaller font)
mobile: 04XX-XXX-XXX (I will give details to the winner to add)
website: www.quorvial.com.au
email: info@quorvial.com.au
COPY FOR LETTERHEAD
Logo
Company Name
Please, submit your designs that include business card, letterhead and envelope. Once selected the winner will be asked to complete the project by creating the rest of the artwork.
FINAL FILES
Print ready files to be supplied as well as Indesign files so that minor amends can be made if necessary in future.
• Layered vectors in EPS & PDF
• Screen quality JPEG & PNGs
ABOUT THE BUSINESS: QUORVIAL
I work with clients to understand their business challenges, developing and executing measurable marketing strategies tied to key business metrics. Services include:
Services include:
• Business planning and business development
• Marketing and brand strategy
• Insight-driven integrated campaigns
• Loyalty programs and retention marketing
• Marketing automation
• Direct marketing (traditional and digital)
• Content strategy and development
Hi everyone,
Target Market(s)
Corporate decision makers (heads of marketing, general managers etc) and small to medium sized business owners. Predominately male aged 35+
Industry/Entity Type
Marketing
Requirements
Must have
- BRAND PERSONALITY
The successful design will communicate brand personality. I am a professional, results-driven entrepreneur, but want to show off my creative flair.
MEMORABILITY
Looking for a unique and eye-catching design. Am considering special printing effects (die cuts, letterpress, interactive elements, embossing, foiling etc) or a striking minimalist approach.
Nice to have
- I have a mission that could be incorporated on reverse if room -
Turning insights into actions & passion into profit.
Should not have
- Use of pink or green.

```html
<!DOCTYPE html>
<html lang="en">
<head>
<meta charset="utf-8">
<title>Quorvial Stationery</title>
<link href="https://fonts.googleapis.com/css2?family=Ubuntu:wght@400;500;700&display=swap" rel="stylesheet">
<style>
  :root {
    --bg: #a9a9a9;
    --paper: #f7f7f7;
    --ink: #1e1e1e;
    --ink-soft: #555555;
    --band: #262626;
    --band-text: #e8e8e8;
    --faint: #e6e6e6;
    --window: #cfcfcf;
    --accent: #2b6fd6;
  }
  * { box-sizing: border-box; margin: 0; padding: 0; }
  html, body { width: 1200px; height: 720px; overflow: hidden; }
  body {
    background: var(--bg);
    font-family: "Ubuntu", sans-serif;
    color: var(--ink);
    position: relative;
  }
  .sheet { position: absolute; background: var(--paper); box-shadow: 0 6px 18px rgba(0,0,0,.25); overflow: hidden; }

  .brand { display: flex; flex-direction: column; }
  .brand-name { display: flex; align-items: center; gap: 6px; font-weight: 700; letter-spacing: .04em; color: var(--ink); white-space: nowrap; }
  .brand-dot { border-radius: 50%; background: var(--ink); flex: none; }
  .brand-tagline { font-weight: 500; text-transform: uppercase; letter-spacing: .02em; color: var(--ink-soft); white-space: nowrap; }

  /* Letterhead */
  .letterhead { left: 40px; top: 40px; width: 452px; height: 640px; }
  .letterhead .brand { position: absolute; left: 40px; top: 40px; }
  .letterhead .brand-name { font-size: 22px; }
  .letterhead .brand-dot { width: 14px; height: 14px; }
  .letterhead .brand-tagline { font-size: 7.5px; margin-top: 3px; }
  .letterhead-watermark {
    position: absolute; left: 0; right: 0; top: 270px;
    text-align: center; font-size: 64px; font-weight: 700; letter-spacing: .04em;
    color: var(--faint); white-space: nowrap;
  }
  .letterhead-footer {
    position: absolute; left: 0; right: 0; bottom: 0; height: 34px;
    background: var(--band); color: var(--band-text);
    display: flex; align-items: center; justify-content: center; gap: 10px;
    font-size: 8.5px; white-space: nowrap;
  }
  .letterhead-footer b { font-weight: 700; }

  /* Business cards */
  .card { top: 40px; width: 290px; height: 166px; }
  .card-back { left: 540px; background: var(--band); color: var(--band-text); display: flex; flex-direction: column; align-items: center; justify-content: center; }
  .card-back .brand { align-items: center; }
  .card-back .brand-name { font-size: 22px; color: var(--band-text); }
  .card-back .brand-dot { width: 13px; height: 13px; background: var(--band-text); }
  .card-back .brand-tagline { font-size: 6.5px; color: #b9b9b9; margin-top: 3px; }
  .card-back-web { position: absolute; bottom: 14px; font-size: 8px; color: #b9b9b9; letter-spacing: .05em; }
  .card-front { left: 850px; display: flex; }
  .card-front-brand { width: 50%; display: flex; align-items: center; justify-content: center; }
  .card-front .brand-name { font-size: 15px; }
  .card-front .brand-dot { width: 9px; height: 9px; }
  .card-front .brand-tagline { font-size: 4.5px; margin-top: 2px; }
  .card-front-details { width: 50%; padding: 34px 14px 0 10px; border-left: 1px solid var(--faint); font-size: 6.5px; line-height: 1.6; color: var(--ink-soft); white-space: nowrap; }
  .card-name { font-size: 10px; font-weight: 500; color: var(--accent); line-height: 1.2; }
  .card-front-details b { color: var(--ink); }
  .card-front-tab { position: absolute; right: 0; top: 34px; width: 5px; height: 16px; background: var(--accent); }

  /* Envelopes */
  .envelope .brand-name { font-size: 20px; }
  .envelope .brand-dot { width: 12px; height: 12px; }
  .envelope .brand-tagline { font-size: 6.5px; margin-top: 3px; }
  .envelope-address { position: absolute; font-size: 7px; line-height: 1.6; color: var(--ink-soft); white-space: nowrap; }
  .envelope-address b { color: var(--ink); }
  .envelope-window { left: 540px; top: 236px; width: 600px; height: 210px; }
  .envelope-window .brand { position: absolute; left: 28px; top: 28px; }
  .envelope-window-pane { position: absolute; right: 28px; top: 22px; width: 180px; height: 70px; border-radius: 10px; background: var(--window); }
  .envelope-window-rule { position: absolute; left: 28px; right: 230px; top: 96px; height: 1px; background: var(--ink-soft); }
  .envelope-window .envelope-address { left: 28px; bottom: 20px; }
  .envelope-plain { left: 540px; top: 462px; width: 600px; height: 218px; }
  .envelope-plain .brand { position: absolute; left: 28px; top: 30px; }
  .envelope-plain .envelope-address { left: 28px; bottom: 24px; }
</style>
</head>
<body>

  <section class="sheet letterhead">
    <div class="brand">
      <div class="brand-name"><span class="brand-dot"></span>QUORVIAL</div>
      <div class="brand-tagline">Clear Strategy. Lasting Growth.</div>
    </div>
    <div class="letterhead-watermark" aria-hidden="true">QUORVIAL</div>
    <footer class="letterhead-footer">
      <span>quorvial Limited</span>
      <span><b>Mobile:</b> 04XX-XXX-XXX</span>
      <span><b>website:</b> www.quorvial.com.au</span>
      <span><b>email:</b> info@quorvial.com.au</span>
    </footer>
  </section>

  <section class="sheet card card-back">
    <div class="brand">
      <div class="brand-name"><span class="brand-dot"></span>QUORVIAL</div>
      <div class="brand-tagline">Clear Strategy. Lasting Growth.</div>
    </div>
    <div class="card-back-web">www.quorvial.com.au</div>
  </section>

  <section class="sheet card card-front">
    <div class="card-front-brand">
      <div class="brand">
        <div class="brand-name"><span class="brand-dot"></span>QUORVIAL</div>
        <div class="brand-tagline">Clear Strategy. Lasting Growth.</div>
      </div>
    </div>
    <div class="card-front-details">
      <div class="card-name">Your Name</div>
      <div>Position</div>
      <div>B Comm, Grad Cert Brand Strategy, CMP</div>
      <div><b>Mobile:</b> 04XX-XXX-XXX</div>
      <div><b>Email:</b> info@quorvial.com.au</div>
    </div>
    <div class="card-front-tab"></div>
  </section>

  <section class="sheet envelope envelope-window">
    <div class="brand">
      <div class="brand-name"><span class="brand-dot"></span>QUORVIAL</div>
      <div class="brand-tagline">Clear Strategy. Lasting Growth.</div>
    </div>
    <div class="envelope-window-rule"></div>
    <div class="envelope-window-pane"></div>
    <div class="envelope-address">
      <div>B Comm, Grad Cert Brand Strategy, CMP</div>
      <div><b>Mobile:</b> 04XX-XXX-XXX</div>
      <div><b>Email:</b> info@quorvial.com.au</div>
    </div>
  </section>

  <section class="sheet envelope envelope-plain">
    <div class="brand">
      <div class="brand-name"><span class="brand-dot"></span>QUORVIAL</div>
      <div class="brand-tagline">Clear Strategy. Lasting Growth.</div>
    </div>
    <div class="envelope-address">
      <div>B Comm, Grad Cert Brand Strategy, CMP</div>
      <div><b>Mobile:</b> 04XX-XXX-XXX</div>
      <div><b>Email:</b> info@quorvial.com.au</div>
    </div>
  </section>

</body>
</html>
```